Anzeigengestaltung Serviceblock
Sehr serviceorientiert, zügig und kreativ!
Zielgruppe
Wir sind eine klassische Steuerberatungsgesellschaft und richten uns vor allem an mittelständische Unternehmen und an das Handwerk. Zu finden sind wir unter www.fiskoralo.de.
Aufgabenstellung
Wir beabsichtigen eine regelmäßige monatliche Werbung mittels eines Serviceblocks in regionalen Zeitungen. Dazu wollen wir eine Art Rahmendesign, dass immer gleich aussieht, von uns aber mit wechselnden Info- Texten gefüllt werden kann. Das Design soll an das Design unserer Homepage angelehnt sein und unser Logo umfassen. Zudem sollen unsere Kontaktdaten gut zu ersehen sein. Muster solcher Serviceblöcke laden wir hoch - die sind aber nicht unbedingt unser Geschmack. Das Maß der Anzeige soll 325 mm breit und 163 mm hoch sein. Wir benötigen das Design als pdf, jpg und sonstiges zeitungskompatibles Format.

```html
<!DOCTYPE html>
<html lang="de">
<head>
<meta charset="utf-8">
<title>Fiskoralo – Serviceblock</title>
<link href="https://fonts.googleapis.com/css2?family=Open+Sans:wght@400;600;700&display=swap" rel="stylesheet">
<style>
  :root {
    --teal-dark: #0d5c66;
    --teal-box: rgba(28, 108, 118, 0.9);
    --teal-line: #1a7380;
    --text-dark: #333333;
    --text-body: #3c3c3c;
    --divider: #cfcfcf;
    --paper: #ffffff;
    --backdrop: #e6e6e6;
  }
  * { box-sizing: border-box; margin: 0; padding: 0; }
  html, body {
    width: 980px; height: 1200px; overflow: hidden;
    background: var(--backdrop);
    font-family: "Open Sans", Arial, sans-serif;
  }
  .ad {
    position: absolute; left: 0; top: 354px;
    width: 980px; height: 491px;
    background: var(--paper);
    overflow: hidden;
  }
  .photo-area {
    position: absolute; left: 603px; top: 0; width: 377px; height: 463px;
    background: linear-gradient(150deg, #6b5a48 0%, #8a8478 30%, #4f6e82 60%, #3c4a52 100%);
  }
  .feature-box {
    position: absolute; left: 522px; top: 92px; width: 257px; height: 299px;
    background: var(--teal-box);
    color: #fff;
    padding: 34px 20px 0 36px;
  }
  .feature-title {
    font-size: 25px; font-weight: 600; letter-spacing: 0.5px; line-height: 1;
  }
  .feature-text {
    margin-top: 36px; font-size: 12.4px; line-height: 17px;
  }
  .brand {
    position: absolute; left: 47px; top: 52px;
    display: flex; align-items: center; gap: 10px;
  }
  .brand-dot {
    width: 30px; height: 30px; border-radius: 50%;
    background: var(--teal-line);
  }
  .brand-name {
    font-size: 27px; font-weight: 600; color: var(--teal-line); letter-spacing: 1px;
  }
  .headline {
    position: absolute; left: 46px; top: 851px; /* reset below */
  }
  .ad .headline {
    top: 142px; font-size: 14.7px; font-weight: 700; color: var(--text-dark); letter-spacing: 0.2px;
  }
  .column {
    position: absolute; top: 183px; width: 216px;
    font-size: 10.7px; line-height: 13.8px; color: var(--text-body);
    text-align: justify; hyphens: auto;
  }
  .column-left { left: 47px; }
  .column-right { left: 281px; }
  .column-sub { font-weight: 600; color: var(--text-dark); text-align: left; }
  .contact-row {
    position: absolute; left: 47px; top: 426px;
    display: flex; align-items: center;
    font-size: 8.4px; line-height: 11px; color: var(--text-body);
  }
  .contact-item { display: flex; align-items: center; gap: 9px; }
  .contact-item svg { flex: none; }
  .contact-divider {
    width: 1px; height: 20px; background: var(--divider); margin: 0 22px;
  }
  .footer-band {
    position: absolute; left: 0; bottom: 0; width: 980px; height: 28px;
    background: var(--teal-dark);
  }
  .footer-url {
    position: absolute; right: 22px; top: 5px;
    color: #fff; font-size: 13.5px; letter-spacing: 0.6px;
  }
</style>
</head>
<body>
  <div class="ad">
    <div class="photo-area" role="img" aria-label="Foto: Frau arbeitet am Laptop an einer Bartheke mit Geschirr"></div>

    <div class="feature-box">
      <h2 class="feature-title">LOREM IPSUM</h2>
      <p class="feature-text">Lorem ipsum dolor sit amet, consectetuer adipiscing elit. Aenean commodo ligula eget dolor. Aenean massa. Cum sociis natoque penatibus et magnis dis parturient montes, nascetur ridiculus mus. Donec quam felis, ultricies nec, pellentesque eu, pretium quis, sem.</p>
    </div>

    <div class="brand">
      <span class="brand-dot"></span>
      <span class="brand-name">FISKORALO</span>
    </div>

    <h1 class="headline">LOREM IPSUM DOLOR SIT AMET</h1>

    <div class="column column-left">
      <p class="column-sub">Lorem ipsum</p>
      <p>Aenean commodo ligula eget dolor. Aenean massa. Cum sociis natoque penatibus et magnis dis parturient montes, nascetur ridiculus mus. Donec quam felis, ultricies nec, pellentesque eu, pretium quis, sem. Nulla consequat massa quis enim. Donec pede justo, fringilla vel, aliquet nec, vulputa&shy;te eget, arcu. In enim justo, rhoncus ut, imperdiet a, venenatis vitae, justo. Nullam dictum felis eu pede mollis pretium. Integer tincidunt. Cras dapibus. Vivamus elemen&shy;tum semper nisi. Aenean vulputate eleifend tellus. Aenean leo ligula, porttitor eu, conse&shy;quat vitae, eleifend ac, enim.</p>
    </div>

    <div class="column column-right">
      <p>Cras dapibus. Vivamus elementum semper nisi. Aenean vulputate eleifend tellus. Aenean leo ligula, porttitor eu, consequat vitae, eleifend ac, enim. Aliquam lorem ante, dapibus in, viverra quis, feugiat a, tellus. Phasellus viverra nulla ut metus varius laoreet. Quisque rutrum. Aenean imperdiet. Etiam ultricies nisi vel augue. rutrum. Aenean imperdiet. Etiam ultricies nisi vel augue. Curabitur ullamcorper ultricies nisi. Nam eget dui. Etiam rhoncus. Maecenas tempus, tellus eget condimen&shy;tum rhoncus, sem quam semper libero, sit amet adipiscing sem neque sed ipsum.</p>
    </div>

    <div class="contact-row">
      <div class="contact-item">
        <svg width="17" height="13" viewBox="0 0 17 13" aria-hidden="true">
          <rect x="0.7" y="0.7" width="15.6" height="11.6" rx="1.5" fill="none" stroke="var(--teal-line)" stroke-width="1.2"/>
          <path d="M1 1.5 L8.5 7.5 L16 1.5" fill="none" stroke="var(--teal-line)" stroke-width="1.2"/>
        </svg>
        <span>E-Mail:<br>info@fiskoralo.de</span>
      </div>
      <span class="contact-divider"></span>
      <div class="contact-item">
        <svg width="16" height="16" viewBox="0 0 24 24" aria-hidden="true">
          <path d="M6.6 2.5 L9.5 6.8 L7.6 9.2 C8.8 11.8 12 15 14.8 16.4 L17.2 14.5 L21.5 17.4 L19.6 21 C12 21 3 12 3 4.4 Z" fill="none" stroke="var(--teal-line)" stroke-width="1.5" stroke-linejoin="round"/>
        </svg>
        <span>Telefon:<br>04721 5580342</span>
      </div>
      <span class="contact-divider"></span>
      <div class="contact-item">
        <svg width="14" height="19" viewBox="0 0 14 19" aria-hidden="true">
          <path d="M7 18 C7 18 1 11 1 7 A6 6 0 0 1 13 7 C13 11 7 18 7 18 Z" fill="none" stroke="var(--teal-line)" stroke-width="1.2"/>
          <circle cx="7" cy="7" r="2.2" fill="none" stroke="var(--teal-line)" stroke-width="1.2"/>
        </svg>
        <span>Anschrift:<br>Am Lindenhang 7, 54311 Wendelsberg</span>
      </div>
    </div>

    <div class="footer-band">
      <span class="footer-url">www.fiskoralo.de</span>
    </div>
  </div>
</body>
</html>
```